New travel store signage for Kelvane Journeys to attract luxury travellers.

Hello,
We are looking to change the signage of our stores. The signage must include the following:
1. Kelvane Journeys Logo (attached)
2. The text...The Travel & Cruise Experts
3. Brand Colours ( Fb0196, 412266, d41d84 and ffffff)
Please note the signage design must be central and only cover two thirds of the store front. We have also attached an image of one of our new stores which might be helpful when preparing a mock up.

We are looking for a quick turnaround on this, making a decision within 48 hours.

Target Market(s)

Retail

Industry/Entity Type

Travel Agency

Font styles to use
Other font styles liked:
• Radley

Colors
E54698
E96AAD
F1A4CE
F9D9EA
FCEFF6
6B429C
8869AF
B7A5CE
E3DAEB
F3F0F8

Requirements
Must have
• Hello, We are looking to change the signage of our stores. The signage must include the following: 1. Kelvane Journeys Logo (attached) 2. The text...The Travel & Cruise Experts 3. Brand Colours ( Fb0196, 412266, d41d84 and ffffff) Please note the signage design must be central and only cover two thirds of the store front.
Should not have
• different colour or fonts. Gradient design.

```html
<!DOCTYPE html>
<html lang="en">
<head>
<meta charset="utf-8">
<title>Kelvane Journeys – Store Signage</title>
<link rel="stylesheet" href="https://fonts.googleapis.com/css2?family=Radley&display=swap">
<style>
  :root {
    --brand-pink: #e8338f;
    --brand-navy: #3b3665;
    --brand-white: #ffffff;
    --frame-grey: #c9c9c9;
    --page-bg: #ffffff;
  }
  * { box-sizing: border-box; margin: 0; padding: 0; }
  html, body {
    width: 1200px;
    height: 856px;
    overflow: hidden;
    background: var(--page-bg);
  }
  .canvas {
    position: relative;
    width: 1200px;
    height: 856px;
    font-family: "Radley", Georgia, serif;
  }
  .sign {
    position: absolute;
    left: 104px;
    width: 998px;
    height: 172px;
  }
  .sign--light {
    top: 236px;
    background: var(--brand-white);
    border: 1.5px solid var(--frame-grey);
    color: var(--brand-navy);
  }
  .sign--dark {
    top: 463px;
    height: 170px;
    background: var(--brand-navy);
    color: var(--brand-white);
  }
  .sign__accent-bar {
    position: absolute;
    left: 0;
    top: 0;
    width: 16px;
    height: 100%;
    background: var(--brand-pink);
  }
  .brand-mark {
    position: absolute;
    left: 128px;
    top: 58px;
    display: flex;
    align-items: center;
    gap: 12px;
  }
  .brand-mark__dot {
    width: 52px;
    height: 52px;
    border-radius: 50%;
    background: var(--brand-pink);
    flex: none;
  }
  .brand-mark__name {
    font-size: 21px;
    white-space: nowrap;
  }
  .sign__divider {
    position: absolute;
    left: 398px;
    top: 42px;
    width: 2px;
    height: 98px;
    background: var(--brand-pink);
  }
  .sign__title {
    position: absolute;
    left: 424px;
    top: 44px;
    font-size: 54px;
    line-height: 1;
    font-weight: 400;
    white-space: nowrap;
  }
  .sign__tagline {
    position: absolute;
    left: 426px;
    top: 112px;
    font-size: 27px;
    line-height: 1;
    letter-spacing: 1px;
    white-space: nowrap;
  }
</style>
</head>
<body>
<main class="canvas">
  <section class="sign sign--light" aria-label="Signage on white">
    <div class="brand-mark">
      <span class="brand-mark__dot"></span>
      <span class="brand-mark__name">Kelvane Journeys</span>
    </div>
    <span class="sign__divider"></span>
    <h1 class="sign__title">Kelvane Journeys</h1>
    <p class="sign__tagline">The Travel &amp; Cruise Experts</p>
  </section>

  <section class="sign sign--dark" aria-label="Signage on navy">
    <span class="sign__accent-bar"></span>
    <div class="brand-mark">
      <span class="brand-mark__dot"></span>
      <span class="brand-mark__name">Kelvane Journeys</span>
    </div>
    <span class="sign__divider"></span>
    <h2 class="sign__title">Kelvane Journeys</h2>
    <p class="sign__tagline">The Travel &amp; Cruise Experts</p>
  </section>
</main>
</body>
</html>
```